Creating High Performance Leadership Teams

I periodically write articles that I sent out to executive and Senior leaders. They should be reproducable in print form yet most of them will go out in pdf Format. I have attached a recent example that we did and I would like to see what you can do with the second example I have attached.

The Format should ideally fit in an A3 Format.

Target Market(s)

Executive and Senior Leaders

Industry/Entity Type

Leadership

Font styles to use
Other font styles liked:
• we often use calibri

Requirements
Must have
• Fit on a A3 paper Format, like the example I sent
Nice to have
• Should look highly professional, perhaps picutures or graphics to Support the text, a Little bit like the Maplecroft Trade Quarterly Articles (MTQ) although mine are shorter.
• You will see our Color formatting by visiting our Website, www.cortavo-insight.com

```html
<!DOCTYPE html>
<html lang="en">
<head>
<meta charset="utf-8">
<title>Finding Advantage in Uncertainty</title>
<link href="https://fonts.googleapis.com/css2?family=Carlito:ital,wght@0,400;0,700;1,400;1,700&display=swap" rel="stylesheet">
<style>
:root{
  --ink:#2f3a40;
  --teal:#2b86b3;
  --teal-dark:#1f5f86;
  --green:#5f9b3c;
  --box:#e9ecee;
  --rule:#c9d2d7;
  --paper:#ffffff;
}
*{box-sizing:border-box;margin:0;padding:0}
html,body{width:853px;height:1200px;overflow:hidden;background:var(--paper)}
body{font-family:"Carlito",Calibri,Arial,sans-serif;color:var(--ink);position:relative}
.hero-image{position:absolute;left:330px;top:0;width:523px;height:318px;
  background:linear-gradient(135deg,#c9e2a4 0%,#7fb36a 30%,#3f8f8a 62%,#1f5d86 100%)}
.intro{position:absolute;left:40px;top:16px;width:280px;font-size:9px;line-height:12px}
.title{position:absolute;left:40px;top:110px;width:285px;font-size:38px;line-height:39px;font-weight:700;color:var(--teal)}
.pullquote{position:absolute;left:40px;top:238px;width:280px;font-size:16px;line-height:17px;font-style:italic;font-weight:700;color:var(--teal-dark)}
.byline{position:absolute;left:40px;top:296px;font-size:15px;font-weight:700;color:var(--ink)}
.lead{position:absolute;left:40px;top:328px;width:378px;font-size:9px;line-height:12px}
.fields{position:absolute;left:432px;top:326px;width:408px;height:114px;background:var(--box);padding:8px 12px;font-size:8.6px;line-height:11px}
.fields h2{font-size:11px;color:var(--teal-dark);margin-bottom:4px}
.fields li{list-style:none;margin-bottom:3px;padding-left:9px;position:relative}
.fields li::before{content:"";position:absolute;left:0;top:4px;width:4px;height:4px;background:var(--green)}
.body-columns{position:absolute;left:40px;top:452px;width:800px;height:146px;column-count:2;column-gap:24px;font-size:9.6px;line-height:12.4px;overflow:hidden}
.body-full{position:absolute;left:40px;top:604px;width:800px;height:430px;font-size:9.6px;line-height:12.4px;overflow:hidden}
.body-columns p,.body-full p{margin-bottom:6px}
strong{color:var(--teal-dark)}
.highlight{text-align:center;font-style:italic;font-weight:700;color:var(--teal);font-size:11px;line-height:14px;padding:6px 0;margin:4px 0 8px;border-top:1px solid var(--rule);border-bottom:1px solid var(--rule)}
.author{position:absolute;left:40px;top:1046px;width:800px;height:70px;border-top:1px solid var(--rule);padding-top:10px;display:flex;gap:12px}
.author-photo{width:50px;height:56px;flex:none;background:linear-gradient(160deg,#b9c7cf,#6e8794)}
.author-text{font-size:9px;line-height:12px}
.author-text strong{color:var(--teal-dark)}
.side-credit{position:absolute;left:14px;top:1190px;transform:rotate(-90deg);transform-origin:left top;font-size:8px;color:#7a868c;white-space:nowrap}
.footer-band{position:absolute;left:40px;right:13px;top:1140px;height:4px;background:linear-gradient(90deg,var(--green),var(--teal))}
.footer-name{position:absolute;right:13px;top:1152px;font-size:11px;font-weight:700;color:var(--teal-dark);display:flex;align-items:center;gap:6px}
.footer-name span{width:9px;height:9px;background:var(--green);display:block}
</style>
</head>
<body>
<div class="hero-image" role="img" aria-label="Photograph in green and blue tones suggesting open landscape and change"></div>

<p class="intro">Leaders that recognise, embrace and create meaningful results from uncertainty change faster, innovate more readily and stimulate high performance cultures. The competence and capability to navigate successfully through uncertainty is a clear and defining advantage. Teams that see past the noise spot openings sooner and move with confidence while others hesitate and wait for a certainty that rarely arrives in today's markets.</p>

<h1 class="title">Finding Advantage in Uncertainty</h1>

<p class="pullquote">“Is uncertainty a springboard to opportunities or a pitfall to performance?”</p>
<p class="byline">by Lars Bellweather</p>

<p class="lead">This question is one that comes up again and again in our work with executive and senior leadership teams. When the landscape shifts, some teams freeze while others move with purpose and clarity. What separates the two is rarely talent alone; it is the shared way a team frames ambiguity and acts on it together. Over many years of working alongside leaders in different industries, we have seen that the same patterns return whenever the ground starts to move beneath a business.</p>

<section class="fields">
  <h2>Three Fields in Uncertainty</h2>
  <ul>
    <li><b>Operational Uncertainty.</b> The field where routines and processes are disrupted and teams must adapt quickly while keeping core delivery stable.</li>
    <li><b>Strategic Uncertainty.</b> The field where markets, competitors and customer needs shift, demanding new direction and fresh priorities.</li>
    <li><b>Personal Uncertainty.</b> The field where individuals question their role, capability and future, affecting energy and commitment.</li>
  </ul>
</section>

<section class="body-columns">
  <p>Here are five recommendations to help your senior leaders and their teams actively embrace uncertainty and turn it into a source of energy rather than anxiety:</p>
  <p><strong>1. Set the pace and tone from the top.</strong> Leaders who model calm curiosity give permission for others to explore rather than defend. Talk openly about what you know, what you do not know and how the team will learn its way forward together, step by step.</p>
  <p><strong>2. Make the unknown visible.</strong> Map the assumptions behind current plans and test them regularly. Teams that name their uncertainties early waste less energy on hidden worries and make better, faster decisions when the facts change around them.</p>
  <p><strong>3. Encourage smart experiments.</strong> Small, fast trials create learning without betting the business. Celebrate the insight gained, not only the result achieved, so people keep trying new approaches and share what they discover with colleagues across the organisation.</p>
</section>

<main class="body-full">
  <p><strong>4. Strengthen trust within the team.</strong> Uncertainty tests relationships. Invest time in candid conversations, clear agreements and mutual support so that pressure pulls the team together rather than apart. When members trust each other, they raise concerns early, challenge ideas without fear and commit fully to decisions once they are made.</p>
  <p><strong>5. Link uncertainty to opportunity.</strong> Ask regularly where change opens new space for growth, service or collaboration. Teams that look for upside find it far more often than teams that only guard against risk. Build this question into strategy sessions, reviews and one-to-one conversations until it becomes a natural habit of the whole leadership group.</p>
  <p class="highlight">“These are valuable opportunities to strengthen the team and build a culture that thrives on change.”</p>
  <p>Developing a positive relationship with uncertainty is something every leader can learn. It starts with awareness of our own habits under pressure and continues with deliberate practice in real situations. Some leaders reach for control, others for more data, and others step back entirely. None of these reactions is wrong in itself, yet each can limit the team when it becomes automatic rather than chosen.</p>
  <p>In one leadership team we supported, members admitted that they spent more time protecting past decisions than shaping new ones. By agreeing a simple rhythm of review and reflection, they shifted their meetings from reporting to real problem solving within a single quarter. Energy rose, decisions were made faster and the wider organisation noticed the difference in tone and direction almost immediately.</p>
  <p>The lesson is clear: uncertainty does not disappear, but our response to it can change. High performance teams treat it as information, not as a threat, and use it to sharpen focus and deepen engagement. They accept that plans will need adjusting and build the flexibility to do so without losing sight of purpose, values and the commitments they have made to customers and colleagues.</p>
  <p>As you reflect on your own team, consider where uncertainty is currently holding you back and where it might be quietly offering an advantage you have not yet seized. Which conversations are being avoided? Which assumptions have not been tested for a long time? Where could a small experiment bring new insight within the next few weeks?</p>
  <p>Our invitation is to start the conversation today. Ask your team what they see, what they fear and what they hope for. Listen carefully, share your own view honestly and agree one concrete step you will take together. The answers will point the way to your next step, and the act of asking will already begin to build the confidence your team needs to find advantage in uncertainty.</p>
</main>

<section class="author">
  <div class="author-photo" role="img" aria-label="Portrait photo of the author"></div>
  <p class="author-text"><strong>Lars Bellweather</strong> is a senior partner at Cortavo Insight Partners, a leadership consultancy based in Munich. He works with executive and senior teams across Europe to build high performance leadership cultures.<br>For more information about these offerings or consultation, contact us at www.cortavo-insight.com</p>
</section>

<div class="footer-band"></div>
<div class="footer-name"><span></span>Cortavo Insight Partners</div>
<p class="side-credit">© 2013 Cortavo Insight Partners GmbH</p>
</body>
</html>
```